Company or website name
- Veltrano
- Links to the website
- http://mpbjuristes.ca/
- Describe your company and organization and target audience
- Company secretarial and management for small business.
- The design should have the following
- The model should include :  - 5 pages. - Clean and modern design. - You must use the images are joined and make a mixture between the model of the website to respect and incorporate photos.
- Other Facts

```html
<!DOCTYPE html>
<html lang="fr">
<head>
<meta charset="utf-8">
<title>Veltrano — Marchand Poirier Bélanger</title>
<link rel="stylesheet" href="https://fonts.googleapis.com/css2?family=Open+Sans:wght@300;400;600&family=Libre+Baskerville&display=swap">
<style>
:root{
  --ink:#1b1b1b;
  --hero-dark:#141414;
  --ribbon:#b92d31;
  --accent:#e8a23a;
  --white:#ffffff;
  --staff-bg:#e6e6e6;
  --card:#b9b9b9;
  --card-text:#2a2a2a;
  --muted:#6a6a6a;
  --link-red:#b9383b;
  --footer-bg:#2a2a2a;
  --footer-text:#e6e6e6;
}
*{box-sizing:border-box;margin:0;padding:0}
html,body{width:683px;height:1200px;overflow:hidden}
body{font-family:"Open Sans",Arial,sans-serif;color:var(--ink);position:relative;background:var(--staff-bg)}

.hero{position:absolute;left:0;top:0;width:683px;height:300px;overflow:hidden}
.hero-photo{position:absolute;inset:0;background:
  radial-gradient(ellipse at 62% 45%,#6b4a24 0%,#3a2612 28%,transparent 55%),
  radial-gradient(ellipse at 30% 85%,#4a3116 0%,transparent 45%),
  linear-gradient(180deg,#242424,var(--hero-dark))}
.brand-ribbon{position:absolute;left:22px;top:0;width:135px;height:128px}
.brand-name{position:absolute;left:22px;top:27px;width:135px;text-align:center;color:var(--white);font-size:15px;font-weight:400;letter-spacing:.5px}
.social{position:absolute;left:639px;top:17px;width:23px;height:23px;border-radius:3px;background:#bdbdbd}
.hero-title{position:absolute;left:0;top:133px;width:683px;text-align:center;color:var(--white);font-size:24px;font-weight:400;letter-spacing:2px}
.hero-firm{position:absolute;left:167px;top:182px;width:350px;height:34px;background:rgba(200,200,200,.7);color:var(--ink);text-align:center;line-height:34px;font-size:18px;letter-spacing:1.5px}
.main-nav{position:absolute;left:22px;top:266px;width:639px;display:flex;justify-content:space-between;font-size:15px;font-weight:300;color:var(--white)}
.main-nav a{color:inherit;text-decoration:none}
.main-nav .current{color:var(--accent)}

.staff{position:absolute;left:0;top:300px;width:683px;height:500px;background:var(--staff-bg)}
.section-title{position:absolute;left:0;top:28px;width:683px;text-align:center;font-size:23px;font-weight:300;letter-spacing:2px;color:var(--ink)}
.card{position:absolute;top:87px;width:190px;height:349px;background:var(--card);box-shadow:3px 5px 6px rgba(0,0,0,.35)}
.card:nth-of-type(1){left:22px}
.card:nth-of-type(2){left:246px}
.card:nth-of-type(3){left:470px}
.card-name{position:absolute;left:0;top:20px;width:100%;padding:0 36px;font-size:14px;font-weight:600;letter-spacing:1.6px;line-height:18px;color:var(--ink);text-transform:uppercase}
.card-name.single{text-align:center;padding:0}
.card-photo{position:absolute;left:32px;top:67px;width:125px;height:125px;background:linear-gradient(180deg,#3d3d42,#1f1f22)}
.card-role{position:absolute;left:0;width:100%;text-align:center;font-family:"Libre Baskerville",Georgia,serif;font-size:11px;letter-spacing:1.5px;color:var(--muted)}
.card-tags{position:absolute;left:0;width:100%;text-align:center;font-size:8px;font-weight:400;letter-spacing:.5px;color:var(--muted)}
.card-tags.spaced{word-spacing:8px}
.card-bio{position:absolute;left:8px;width:176px;font-size:9px;line-height:11px;letter-spacing:.5px;color:var(--card-text);height:67px;overflow:hidden}
.card-more{position:absolute;right:25px;font-size:9px;letter-spacing:.6px;color:var(--link-red)}
.pager{position:absolute;left:355px;top:455px;display:flex;font-size:15px;font-weight:300;color:#8d8d8d}
.pager span{width:31.7px}
.pager .current{color:var(--link-red)}

.about{position:absolute;left:0;top:800px;width:683px;height:301px;overflow:hidden}
.about-photo{position:absolute;inset:0;background:
  radial-gradient(ellipse at 20% 40%,#6a6c70 0%,transparent 50%),
  radial-gradient(ellipse at 80% 70%,#5a5c60 0%,transparent 50%),
  linear-gradient(180deg,#3e4044,#34363a)}
.about-title{position:absolute;left:47px;top:26px;font-size:23px;font-weight:300;color:var(--white);padding-bottom:2px;border-bottom:1px solid var(--white);width:101px}
.about-text{position:absolute;left:47px;top:80px;width:605px;font-size:11.3px;line-height:14.3px;color:var(--white)}
.about-text p+p{margin-top:14px}

.site-footer{position:absolute;left:0;top:1101px;width:683px;height:99px;background:var(--footer-bg);color:var(--footer-text)}
.copyright{position:absolute;left:22px;top:3px;font-size:6px}
.footer-col{position:absolute;top:21px;list-style:none;font-size:8.6px;line-height:10.8px}
.footer-col:nth-of-type(1){left:80px}
.footer-col:nth-of-type(2){left:236px}
.footer-col:nth-of-type(3){left:391px}
.footer-col:nth-of-type(4){left:547px}
</style>
</head>
<body>

<header class="hero">
  <div class="hero-photo" role="img" aria-label="Photo of a wooden judge's gavel on a dark background"></div>
  <svg class="brand-ribbon" viewBox="0 0 135 128" aria-hidden="true"><polygon points="0,0 135,0 135,128 67.5,86 0,128" fill="var(--ribbon)"/></svg>
  <div class="brand-name">Veltrano</div>
  <a class="social" href="#" aria-label="Réseau social"></a>
  <h1 class="hero-title">Résoudre votre Puzzle juridique</h1>
  <div class="hero-firm">Marchand Poirier Bélanger</div>
  <nav class="main-nav">
    <a class="current" href="#">Accueil</a>
    <a href="#">Le Cabinet</a>
    <a href="#">Notre Expertise</a>
    <a href="#">Nos Avocats</a>
    <a href="#">Publications</a>
    <a href="#">Jugements</a>
    <a href="#">Nous Joindre</a>
  </nav>
</header>

<section class="staff">
  <h2 class="section-title">MEET OUR STAFF</h2>

  <article class="card">
    <h3 class="card-name single">Marc Gagnon</h3>
    <div class="card-photo" role="img" aria-label="Portrait photo of Marc Gagnon"></div>
    <div class="card-role" style="top:200px">LAWYER</div>
    <div class="card-tags spaced" style="top:220px">Municipal Litige</div>
    <p class="card-bio" style="top:251px">Marc Gagnon has experience of more than twenty-seven (27) years in the field of litigation. He has concentrated his practice in commercial law, civil and criminal liability.</p>
    <span class="card-more" style="top:322px">LIRE LA SUITE</span>
  </article>

  <article class="card">
    <h3 class="card-name">Isabelle<br>Roy</h3>
    <div class="card-photo" role="img" aria-label="Portrait photo of Isabelle Roy"></div>
    <div class="card-role" style="top:203px">LAWYER</div>
    <div class="card-tags" style="top:224px">Legitation Job Municipal</div>
    <p class="card-bio" style="top:256px;height:56px">Isabelle Roy joined the firm in 2016 after having completed her internship and practices mainly in litigation and administrative law. She is regularly called upon to</p>
    <span class="card-more" style="top:325px">LIRE LA SUITE</span>
  </article>

  <article class="card">
    <h3 class="card-name">Olivier<br>Lapointe</h3>
    <div class="card-photo" role="img" aria-label="Portrait photo of Olivier Lapointe"></div>
    <div class="card-role" style="top:203px">LAWYER</div>
    <div class="card-tags" style="top:224px">Legitation Job Municipal</div>
    <p class="card-bio" style="top:256px;height:56px">Olivier Lapointe joined the firm Marchand Poirier Bélanger in 2008. As part of her practice, Mr. Lapointe is called to write opinions, preparing procedures and make</p>
    <span class="card-more" style="top:325px">LIRE LA SUITE</span>
  </article>

  <div class="pager">
    <span class="current">1</span><span>2</span><span>3</span><span>4</span><span>5</span><span>6</span><span>7</span><span>8</span><span>9</span><span>10</span>
  </div>
</section>

<section class="about">
  <div class="about-photo" role="img" aria-label="Painted figure of Lady Justice holding scales and a sword"></div>
  <h2 class="about-title">About Us</h2>
  <div class="about-text">
    <p>Lorem ipsum dolor sit amet, consectetur adipiscing elit. Fusce vitae scelerisque erat. Curabitur elit libero, placerat volutpat dui vel, placerat suscipit dui. Ut pulvinar pharetra lacinia. Etiam nec purus at<br>lacus molestie elementum. Morbi eu metus eget enim maximus facilisis. Ut non risus ac turpis venenatis auctor. Proin pharetra rhoncus nisl, eget faucibus odio accumsan sit amet. Duis elit nisl, faucibus nec nunc eget, fermentum pulvinar lorem. Morbi consectetur aliquam ante sit amet dapibus. Praesent et posuere massa. Pellentesque nec leo est.</p>
    <p>placerat suscipit dui. Ut pulvinar pharetra lacinia. Etiam nec purus at<br>lacus molestie elementum. Morbi eu metus eget enim maximus facilisis. Ut non risus ac turpis venenatis auctor. Proin pharetra rhoncus nisl, eget faucibus odio accumsan sit amet. Duis elit nisl, faucibus nec nunc eget, fermentum pulvinar lorem. Morbi consectetur aliquam ante sit amet dapibus. Praesent et posuere massa. Pellentesque nec leo est.</p>
  </div>
</section>

<footer class="site-footer">
  <p class="copyright">© 1999-2015 Copyright Protected</p>
  <ul class="footer-col"><li>Le Cabinet</li><li>Notre Expertise</li><li>Nos Avocats</li><li>Publications</li><li>Jugements</li><li>Nous Joindre</li></ul>
  <ul class="footer-col"><li>Le Cabinet</li><li>Notre Expertise</li><li>Nos Avocats</li><li>Publications</li><li>Jugements</li><li>Nous Joindre</li></ul>
  <ul class="footer-col"><li>Le Cabinet</li><li>Notre Expertise</li><li>Nos Avocats</li><li>Publications</li><li>Jugements</li><li>Nous Joindre</li></ul>
  <ul class="footer-col"><li>Le Cabinet</li><li>Notre Expertise</li><li>Nos Avocats</li><li>Publications</li><li>Jugements</li><li>Nous Joindre</li></ul>
</footer>

</body>
</html>
```